Northern Tempest Informational Sheet

I need a one page informational sheet (advertisement) for a horse called Northern Tempest. It should have the name Northern Tempest and the content below. It needs to be eye-catching. I have attached 3 examples of what these advertisements look like so it's easier to create. I've also attached 2 pictures of the horse which should both be used in the advertisement.

Here are the bullet points:

- Son of Distant Harbor with total progeny earnings over 13 million dollars
- Ranks among West Virginia top 3 active sires by progeny earnings 2019
- In 9 crops of racing age, has sired 200 winners from 275 starters
- Sired Don Marbellino who earned over $800k racing from age 2 to 7.
- Won 3 of 4 lifetime starts

stands at stud for $1000 at Ashgrove Farm near Charles Town
Call Dwight Kessler - (304) 555-0193

Target Market(s)

Thoroughbred racing people interested in breeding

Requirements
Must have
• Unique and creative. The name of the horse Northern Tempest should be clear and bold, the picture should also be prominent.
Should not have
• Cartoon like, whimsical

```html
<!DOCTYPE html>
<html lang="en">
<head>
<meta charset="utf-8">
<title>Northern Tempest – Stallion Sheet</title>
<link rel="stylesheet" href="https://fonts.googleapis.com/css2?family=Tinos:wght@400;700&family=Open+Sans:wght@400;600;700&display=swap">
<style>
  :root {
    --ink-dark: #0c0c0c;
    --ink-mid: #2b2b2b;
    --ink-light: #4a4a4a;
    --cream: #f3e3c8;
    --silver: #b9b9bb;
    --silver-light: #d6d6d8;
    --crimson: #7a1a1a;
    --gold: #c6a36b;
    --white: #ffffff;
    --photo-sky: #c9c6c0;
    --photo-coat: #7a3e1e;
    --photo-ground: #3f4650;
  }
  * { margin: 0; padding: 0; box-sizing: border-box; }
  html, body { width: 980px; height: 1200px; overflow: hidden; }
  body { background: var(--ink-dark); font-family: "Open Sans", Arial, sans-serif; }

  .sheet {
    position: relative;
    width: 980px;
    height: 1200px;
    overflow: hidden;
    background:
      linear-gradient(180deg, var(--ink-dark) 0%, var(--ink-mid) 18%, var(--ink-dark) 40%, var(--ink-dark) 62%, var(--ink-light) 78%, var(--ink-dark) 100%);
  }
  .sheet__art { position: absolute; inset: 0; width: 980px; height: 1200px; }

  .stallion-name {
    position: absolute;
    top: 18px;
    right: 32px;
    text-align: right;
    font-family: "Tinos", "Times New Roman", serif;
    font-weight: 700;
    font-size: 88px;
    line-height: 0.98;
    color: var(--cream);
    text-shadow: 0 3px 6px rgba(0,0,0,0.6);
  }

  .highlights {
    position: absolute;
    top: 908px;
    left: 108px;
    list-style: none;
  }
  .highlights__item {
    display: flex;
    align-items: center;
    gap: 16px;
    height: 43px;
    font-size: 18.5px;
    color: var(--white);
  }
  .highlights__tick { width: 20px; height: 20px; flex: none; }

  .stud-fee {
    position: absolute;
    right: 32px;
    top: 1112px;
    text-align: right;
    font-family: "Tinos", "Times New Roman", serif;
    font-size: 27px;
    line-height: 1.2;
    color: var(--cream);
  }

  .contact-bar {
    position: absolute;
    left: 0;
    top: 1138px;
    width: 480px;
    height: 42px;
    background: var(--crimson);
    clip-path: polygon(0 0, 100% 0, 94% 100%, 0 100%);
    display: flex;
    align-items: center;
    gap: 12px;
    padding-left: 48px;
    font-size: 18px;
    font-weight: 700;
    color: var(--white);
  }
  .contact-bar__icon { width: 20px; height: 20px; }
</style>
</head>
<body>
<main class="sheet">

  <svg class="sheet__art" viewBox="0 0 980 1200" aria-hidden="true">
    <defs>
      <linearGradient id="silverBand" x1="0" y1="0" x2="1" y2="1">
        <stop offset="0" stop-color="var(--silver-light)"/>
        <stop offset="1" stop-color="var(--silver)"/>
      </linearGradient>
    </defs>
    <polygon points="109,50 980,296 980,340 0,345 0,300" fill="url(#silverBand)"/>
    <polygon points="0,624 384,714 384,730 0,640" fill="var(--silver)"/>
  </svg>

  <svg class="sheet__art" viewBox="0 0 980 1200" role="img" aria-label="Photo of the bay stallion standing in profile beside a brick barn">
    <defs>
      <linearGradient id="mainPhoto" x1="0" y1="0" x2="0" y2="1">
        <stop offset="0" stop-color="var(--photo-sky)"/>
        <stop offset="0.35" stop-color="#9c7d66"/>
        <stop offset="0.6" stop-color="var(--photo-coat)"/>
        <stop offset="1" stop-color="var(--photo-ground)"/>
      </linearGradient>
    </defs>
    <polygon points="144,111 980,319 980,798 384,722 0,631 0,334" fill="url(#mainPhoto)"/>
  </svg>

  <svg class="sheet__art" viewBox="0 0 980 1200" aria-hidden="true">
    <polygon points="384,722 980,798 793,892" fill="var(--crimson)"/>
    <circle cx="224" cy="706" r="160" fill="var(--silver-light)"/>
  </svg>

  <svg class="sheet__art" viewBox="0 0 980 1200" role="img" aria-label="Head and neck portrait of the stallion in a leather halter on a crimson background">
    <defs>
      <radialGradient id="portrait" cx="0.55" cy="0.5" r="0.6">
        <stop offset="0" stop-color="#8a4a22"/>
        <stop offset="0.55" stop-color="#6e2a18"/>
        <stop offset="1" stop-color="var(--crimson)"/>
      </radialGradient>
    </defs>
    <circle cx="224" cy="706" r="144" fill="url(#portrait)"/>
  </svg>

  <h1 class="stallion-name">Northern<br>Tempest</h1>

  <ul class="highlights">
    <li class="highlights__item"><svg class="highlights__tick" viewBox="0 0 20 20"><rect x="2" y="5" width="13" height="13" fill="none" stroke="var(--gold)" stroke-width="1.6"/><path d="M5 11l3.5 3.5L18 3" fill="none" stroke="var(--gold)" stroke-width="2"/></svg>Son of Distant Harbor with total progeny earnings over 13 million dollars</li>
    <li class="highlights__item"><svg class="highlights__tick" viewBox="0 0 20 20"><rect x="2" y="5" width="13" height="13" fill="none" stroke="var(--gold)" stroke-width="1.6"/><path d="M5 11l3.5 3.5L18 3" fill="none" stroke="var(--gold)" stroke-width="2"/></svg>Ranks among West Virginia top 3 active sires by progeny earnings 2019</li>
    <li class="highlights__item"><svg class="highlights__tick" viewBox="0 0 20 20"><rect x="2" y="5" width="13" height="13" fill="none" stroke="var(--gold)" stroke-width="1.6"/><path d="M5 11l3.5 3.5L18 3" fill="none" stroke="var(--gold)" stroke-width="2"/></svg>In 9 crops of racing age, has sired 200 winners from 275 starters</li>
    <li class="highlights__item"><svg class="highlights__tick" viewBox="0 0 20 20"><rect x="2" y="5" width="13" height="13" fill="none" stroke="var(--gold)" stroke-width="1.6"/><path d="M5 11l3.5 3.5L18 3" fill="none" stroke="var(--gold)" stroke-width="2"/></svg>Sired Don Marbellino who earned over $800k racing from age 2 to 7.</li>
    <li class="highlights__item"><svg class="highlights__tick" viewBox="0 0 20 20"><rect x="2" y="5" width="13" height="13" fill="none" stroke="var(--gold)" stroke-width="1.6"/><path d="M5 11l3.5 3.5L18 3" fill="none" stroke="var(--gold)" stroke-width="2"/></svg>Won 3 of 4 lifetime starts</li>
  </ul>

  <p class="stud-fee">STANDS AT STUD FOR $1000<br>at Ashgrove Farm near Charles Town</p>

  <p class="contact-bar">
    <span>Call Dwight Kessler</span>
    <svg class="contact-bar__icon" viewBox="0 0 20 20" aria-hidden="true"><circle cx="10" cy="10" r="8.5" fill="none" stroke="var(--white)" stroke-width="1.6"/><path d="M7 5.5l1.6 2.4-1 1.2c.6 1.3 1.6 2.3 2.9 2.9l1.2-1 2.4 1.6-.8 1.6c-3.8-.3-6.8-3.3-7.1-7.1z" fill="var(--white)"/></svg>
    <span>(304) 555-0193</span>
  </p>

</main>
</body>
</html>
```